Screendesign für neue Website
Zielgruppe
Bauherren und alle die mal zum Architekten müssen.
Aufgabenstellung
Bei diesem Auftrag handelt es sich um die Erstellung eines Screendesigns für eine Website eines Archtiktenbüros.
Es wird daher ein Layout im PSD-Format erwartet, eine Umsetzung dessen in HTML wird nicht gefordert.

```html
<!DOCTYPE html>
<html lang="de">
<head>
<meta charset="utf-8">
<title>Planungsbüro Anton Wiese – Architekten</title>
<link href="https://fonts.googleapis.com/css2?family=Abel&display=swap" rel="stylesheet">
<style>
  :root {
    --header-grey: #9b9b9b;
    --page-black: #000000;
    --nav-bg: #333333;
    --nav-line: #5a5a5a;
    --text-light: #ffffff;
    --accent-green: #8dc63f;
    --logo-ink: #111111;
  }
  * { margin: 0; padding: 0; box-sizing: border-box; }
  html, body { width: 1200px; height: 900px; overflow: hidden; background: var(--page-black); }
  body { font-family: "Abel", sans-serif; color: var(--text-light); }

  .site { position: relative; width: 1200px; height: 900px; background: var(--page-black); }

  .masthead { position: absolute; left: 0; top: 0; width: 1200px; height: 247px; background: var(--header-grey); }

  .brand {
    position: absolute; left: 856px; top: 108px; width: 173px;
    display: flex; align-items: center; gap: 10px;
  }
  .brand-mark { width: 22px; height: 22px; background: var(--accent-green); border-radius: 50%; flex: none; }
  .brand-name { font-size: 20px; line-height: 1.1; color: var(--logo-ink); }

  .gallery {
    position: absolute; left: 0; top: 247px; width: 1200px; height: 173px;
    display: flex; gap: 2px; background: #cfcfcf;
    border-top: 1px solid #bdbdbd; border-bottom: 2px solid #cfcfcf;
  }
  .gallery-tile { position: relative; flex: 1; overflow: hidden; }
  .gallery-tile::after {
    content: ""; position: absolute; left: 0; right: 0; bottom: 0; height: 62px;
    background: rgba(255,255,255,0.16);
  }
  .tile-1 { background: linear-gradient(180deg, #7f9fbf 0%, #dfe6ee 45%, #6d7882 100%); }
  .tile-2 { background: linear-gradient(180deg, #9fb7d4 0%, #3b3f3a 40%, #c89a3c 70%, #8fa7b4 100%); }
  .tile-3 { background: linear-gradient(180deg, #4a63b4 0%, #e4e4e4 45%, #7f93a6 100%); }
  .tile-4 { background: linear-gradient(180deg, #c9ced6 0%, #f2f2f2 50%, #9c9c9c 100%); }
  .tile-5 { background: linear-gradient(180deg, #5f7fa8 0%, #2a2624 45%, #b0632c 75%, #4a4642 100%); }
  .tile-6 { background: linear-gradient(180deg, #cfc4b0 0%, #9b7a52 45%, #e9e2d6 100%); }
  .tile-7 { background: linear-gradient(180deg, #7a9ac6 0%, #8f8f7a 45%, #5d8b4a 75%, #7fb0c4 100%); }

  .main-nav {
    position: absolute; left: 856px; top: 420px; width: 173px; height: 480px;
    background: var(--nav-bg);
  }
  .main-nav ul { list-style: none; padding-top: 26px; }
  .main-nav li { border-bottom: 1px solid var(--nav-line); height: 46px; }
  .main-nav a {
    display: block; padding: 8px 0 0 22px; font-size: 18px;
    color: var(--text-light); text-decoration: none; letter-spacing: -0.2px;
  }
  .main-nav .is-active a { color: var(--accent-green); }

  .claim-emblem {
    position: absolute; left: 132px; top: 612px; width: 134px; height: 134px;
    border-radius: 50%;
    background: radial-gradient(circle closest-side at 50% 50%, #a9dc4a 0%, #7fbb2c 60%, rgba(127,187,44,0.35) 85%, rgba(0,0,0,0) 100%);
  }
  .claim-line { position: absolute; white-space: nowrap; line-height: 1; }
  .claim-line-1 { left: 273px; top: 697px; font-size: 21px; }
  .claim-line-1 .claim-big { font-size: 43px; color: var(--accent-green); }
  .claim-line-2 { left: 182px; top: 748px; font-size: 27px; color: var(--accent-green); }
  .claim-line-2 .claim-big { font-size: 47px; color: var(--text-light); }
  .claim-sep { color: var(--accent-green); margin: 0 6px; font-size: 21px; }
</style>
</head>
<body>
<div class="site">
  <header class="masthead">
    <div class="brand">
      <span class="brand-mark"></span>
      <span class="brand-name">Planungsbüro<br>Anton Wiese</span>
    </div>
  </header>

  <section class="gallery" aria-label="Projektgalerie">
    <div class="gallery-tile tile-1" role="img" aria-label="Foto: moderne weiße Villa mit Glasfront"></div>
    <div class="gallery-tile tile-2" role="img" aria-label="Foto: Terrasse mit Pool am Meer"></div>
    <div class="gallery-tile tile-3" role="img" aria-label="Foto: beleuchtetes Haus mit Pool bei Dämmerung"></div>
    <div class="gallery-tile tile-4" role="img" aria-label="Foto: heller Wohnraum unter Satteldach"></div>
    <div class="gallery-tile tile-5" role="img" aria-label="Foto: Haus mit Glasgiebel am Abend"></div>
    <div class="gallery-tile tile-6" role="img" aria-label="Foto: Wohnzimmer mit Kamin und Holzdecke"></div>
    <div class="gallery-tile tile-7" role="img" aria-label="Foto: Flachdachhaus mit Pool vor Bergen"></div>
  </section>

  <nav class="main-nav">
    <ul>
      <li><a href="#">Unternehmen</a></li>
      <li><a href="#">Projekte</a></li>
      <li class="is-active"><a href="#">Information</a></li>
      <li><a href="#">Aktuelles</a></li>
      <li><a href="#">Leistungen</a></li>
      <li><a href="#">Kontakt</a></li>
    </ul>
  </nav>

  <div class="claim-emblem" role="img" aria-label="Illustration: grünes vierblättriges Kleeblatt"></div>
  <p class="claim-line claim-line-1">Architekten schaffen<span class="claim-sep">::</span><span class="claim-big">Lebens-Raum</span></p>
  <p class="claim-line claim-line-2">Lebens-Traum<span class="claim-sep">::</span><span class="claim-big">Traumhaus</span></p>
</div>
</body>
</html>
```